Lantern Business Cards

Need business cards for my employees at my restaurant.

Needs to include:
Our Logo
Lantern Bowls & Brews
Name: Nora Pettigrew
Title : Owner
Address: 487 Mirella Ave. Marlowe Springs, KS 86519
Web: www.lanternkestrel.com
Phone: 555-210-0147
Cell: 555-210-0192
Email: info@lanternkestrel.com

```html
<!DOCTYPE html>
<html lang="en">
<head>
<meta charset="utf-8">
<title>Lantern Bowls &amp; Brews — Business Card</title>
<link rel="stylesheet" href="https://fonts.googleapis.com/css2?family=Josefin+Sans:wght@300;400;600;700&display=swap">
<style>
  :root {
    --backdrop: #1b1b1b;
    --card: #ffffff;
    --card-edge: #f1f1f1;
    --ink: #1a1a1a;
    --band: #161616;
    --brand-red: #c8354a;
    --muted: #6a6a6a;
    --light-text: #f2f2f2;
  }
  * { box-sizing: border-box; margin: 0; padding: 0; }
  html, body {
    width: 1200px; height: 900px; overflow: hidden;
    background: var(--backdrop);
    font-family: "Josefin Sans", sans-serif;
  }
  .card {
    position: absolute; left: 100px; top: 165px;
    width: 1000px; height: 570px;
    background: linear-gradient(135deg, var(--card) 60%, var(--card-edge));
    overflow: hidden;
  }
  .brand { position: absolute; left: 70px; top: 58px; }
  .brand-name {
    display: flex; align-items: center; gap: 14px;
    color: var(--brand-red); font-weight: 700; font-size: 64px;
    letter-spacing: 2px; text-transform: uppercase; line-height: 1;
  }
  .brand-dot { width: 34px; height: 34px; border-radius: 50%; background: var(--brand-red); }
  .brand-tagline {
    margin-top: 10px; padding-top: 8px;
    border-top: 2px solid var(--ink);
    width: 330px; text-align: center;
    color: var(--ink); font-size: 15px; font-weight: 600;
    letter-spacing: 2px; text-transform: uppercase;
  }
  .band-contact {
    position: absolute; left: 0; top: 250px;
    width: 640px; height: 270px; background: var(--band);
  }
  .band-corner {
    position: absolute; left: 640px; top: 380px;
    width: 360px; height: 140px; background: var(--band);
  }
  .badge-circle {
    position: absolute; left: 520px; top: 320px;
    width: 240px; height: 240px; border-radius: 50%;
    background: var(--card);
  }
  .contact-list { position: absolute; left: 40px; top: 272px; list-style: none; }
  .contact-list li {
    display: flex; align-items: center; gap: 14px;
    height: 42px; color: var(--light-text);
    font-size: 20px; font-weight: 300; letter-spacing: 0.5px;
  }
  .contact-icon {
    width: 26px; height: 26px; border-radius: 50%;
    background: var(--brand-red);
    display: flex; align-items: center; justify-content: center; flex: none;
  }
  .address {
    position: absolute; left: 350px; top: 276px;
    color: var(--light-text); font-size: 21px; font-weight: 300; font-style: normal;
    line-height: 1.45; letter-spacing: 0.5px;
  }
  .person { position: absolute; right: 50px; top: 270px; }
  .person-name { color: var(--brand-red); font-size: 34px; font-weight: 600; letter-spacing: 0.5px; }
  .person-title { margin-top: 4px; color: var(--muted); font-size: 21px; font-weight: 300; }
</style>
</head>
<body>
  <article class="card">
    <header class="brand">
      <div class="brand-name"><span class="brand-dot"></span>Lantern</div>
      <div class="brand-tagline">Bowls and Brews</div>
    </header>

    <div class="band-contact"></div>
    <div class="band-corner"></div>
    <div class="badge-circle"></div>

    <ul class="contact-list">
      <li>
        <span class="contact-icon">
          <svg width="14" height="14" viewBox="0 0 24 24" fill="#fff"><path d="M6.6 10.8a15.1 15.1 0 0 0 6.6 6.6l2.2-2.2a1 1 0 0 1 1-.25 11.4 11.4 0 0 0 3.6.57 1 1 0 0 1 1 1V20a1 1 0 0 1-1 1A17 17 0 0 1 3 4a1 1 0 0 1 1-1h3.5a1 1 0 0 1 1 1c0 1.25.2 2.45.57 3.6a1 1 0 0 1-.25 1z"/></svg>
        </span>555-210-0147
      </li>
      <li>
        <span class="contact-icon">
          <svg width="14" height="14" viewBox="0 0 24 24" fill="none" stroke="#fff" stroke-width="2.2"><rect x="7" y="2" width="10" height="20" rx="2"/><line x1="11" y1="18" x2="13" y2="18"/></svg>
        </span>555-210-0192
      </li>
      <li>
        <span class="contact-icon">
          <svg width="14" height="14" viewBox="0 0 24 24" fill="none" stroke="#fff" stroke-width="2.2"><rect x="3" y="5" width="18" height="14" rx="1"/><path d="M3 6l9 7 9-7"/></svg>
        </span>info@lanternkestrel.com
      </li>
      <li>
        <span class="contact-icon">
          <svg width="14" height="14" viewBox="0 0 24 24" fill="none" stroke="#fff" stroke-width="2"><circle cx="12" cy="12" r="9"/><path d="M3 12h18M12 3c3 3 3 15 0 18M12 3c-3 3-3 15 0 18"/></svg>
        </span>www.lanternkestrel.com
      </li>
    </ul>

    <address class="address">
      487 Mirella Ave.<br>
      Marlowe Springs<br>
      KS 86519
    </address>

    <div class="person">
      <div class="person-name">Nora Pettigrew</div>
      <div class="person-title">Owner</div>
    </div>
  </article>
</body>
</html>
```